Pressline Design Project For Budget Hotel

Although it is a budget hotel we would like a mid to upmarket word press web design with relatively prominent images of local attractions. The design needs to be clean and professional looking.

This is design only. The design/files most be easy for our developer to work with and develop the back end/code.

The website will contain 6 pages:
Homepage
Accommodation & Rates
Facilities
Attractions
Bookings
Contact us

The full content is provided in a word doc which i have uploaded along with all the images needed.

Target Market(s)

The target audience are budget travelers looking for clean and comfortable accommodation at an affordable price.

Industry/Entity Type

Hotel

Requirements
Must have
• Prominent images of local attractions in a changing background or as a sliding banner.

Quantel Hotel Reservation booking form. A small one on the home page and full one on the booking page.

Google maps window in the contact page
Should not have
• We dont want to many bright colours (ie yellow, red) but clean white is fine

```html
<!DOCTYPE html>
<html lang="en">
<head>
<meta charset="utf-8">
<title>Harbourside Hotel Linden</title>
<link rel="stylesheet" href="https://fonts.googleapis.com/css2?family=Rokkitt:wght@400;500;700&display=swap">
<style>
:root{
  --orange:#ff6a00;
  --ink:#444444;
  --nav:#555555;
  --nav-dark:#333333;
  --page:#f6f6f6;
  --backdrop:#4a4a4a;
  --rule:#dcdcdc;
}
*{margin:0;padding:0;box-sizing:border-box}
html,body{width:1022px;height:1200px;overflow:hidden}
body{background:radial-gradient(ellipse at 50% 40%,#777 0%,var(--backdrop) 60%,#333 100%);font-family:Arial,Helvetica,sans-serif;color:var(--ink);position:relative}
.sheet{position:absolute;left:87px;top:0;width:848px;height:1182px;background:var(--page)}
.abs{position:absolute}
.display{font-family:'Rokkitt',serif}
.brand{left:18px;top:30px;font-size:37px;letter-spacing:1px;color:var(--ink);font-weight:400}
.brand span{color:var(--orange)}
.contact{left:636px;font-size:13px;font-family:'Rokkitt',serif;letter-spacing:.5px;display:flex;align-items:center;gap:6px}
.contact svg{width:12px;height:12px}
.offer{right:20px;top:56px;font-size:28px;font-family:'Rokkitt',serif;letter-spacing:.5px;color:var(--ink)}
.offer b{color:var(--orange);font-size:33px;font-weight:700}
.nav{left:9px;top:101px;width:822px;height:37px;background:var(--nav);border-top:3px solid #777;display:flex;list-style:none}
.nav li{color:#fff;font-family:'Rokkitt',serif;font-size:12.5px;display:flex;align-items:center;justify-content:center;border-right:1px solid #777;letter-spacing:.4px}
.nav li.active{background:var(--nav-dark);border-top:3px solid var(--orange);margin-top:-3px}
.slider{left:9px;top:163px;width:823px;height:364px;background:linear-gradient(150deg,#9a9a96 0%,#6d6b68 35%,#8b2a2c 60%,#b8141c 78%,#3a3a3a 100%)}
.shadow{left:30px;top:527px;width:780px;height:18px;background:radial-gradient(ellipse at 50% 0%,rgba(0,0,0,.22),rgba(0,0,0,0) 70%)}
.booking{left:28px;top:238px;width:239px;height:149px;background:rgba(50,50,50,.75);border:1px solid #666}
.field{position:absolute;background:#fff;height:21px;font-size:11px;color:#aaa;padding:4px 6px}
.field svg{position:absolute;right:4px;top:5px}
.btn-book{left:155px;top:103px;width:79px;height:26px;background:var(--orange);color:#fff;border-radius:8px;font-family:'Rokkitt',serif;font-size:14px;display:flex;align-items:center;justify-content:center}
.section-title{left:9px;top:572px;width:823px;height:34px;display:flex;align-items:center;gap:8px}
.section-title:before,.section-title:after{content:"";flex:1;height:1px;background:var(--rule)}
.section-title h2{font-family:'Rokkitt',serif;font-weight:400;font-size:29px;letter-spacing:1.5px;color:var(--ink)}
.about{left:16px;width:816px;font-size:12.5px;line-height:15.5px;text-align:center}
.about.clip{top:612px;height:31px;overflow:hidden}
.about.full{top:653px}
.more{background:var(--orange);color:#fff;font-family:'Rokkitt',serif;display:flex;align-items:center;justify-content:center;gap:8px}
.more.lg{left:354px;top:728px;width:136px;height:29px;font-size:19px}
.more.sm{width:98px;height:24px;font-size:13px}
.card{width:245px}
.card h3{font-family:'Rokkitt',serif;font-weight:500;font-size:19px;letter-spacing:1px;color:var(--ink)}
.card .rule{height:2px;background:var(--rule);margin-top:10px;width:210px;position:relative}
.card .rule:before{content:"";position:absolute;left:0;top:0;width:66px;height:4px;margin-top:-1px;background:var(--orange)}
.frame{margin-top:14px;width:243px;height:125px;background:#ccc;padding:6px}
.frame div{width:100%;height:100%;border:1px solid #fff}
.card p{margin-top:9px;font-size:11px;line-height:15.4px;text-align:justify}
.card p b{color:#555}
.card .more{margin-left:auto;margin-top:10px}
.footer{left:15px;top:1147px;width:824px;height:35px;background:var(--nav);color:#fff;font-size:10px;display:flex;align-items:center;justify-content:space-between;padding:0 12px}
.footer nav span{margin-left:8px}
.footer nav i{font-style:normal;margin-left:8px}
</style>
</head>
<body>
<div class="sheet">
  <div class="abs brand display">Harbourside <span>Hotel</span> Linden</div>

  <div class="abs contact" style="top:5px">
    <svg viewBox="0 0 12 12"><rect width="12" height="12" rx="2" fill="#ff6a00"/><path d="M4 3l1.2 1.5-.7.8a5 5 0 0 0 2.2 2.2l.8-.7L9 8l-.8 1.2C6 9 3.2 6 3 3.8z" fill="#fff"/></svg>
    +61-200-555-0148
  </div>
  <div class="abs contact" style="top:25px">
    <svg viewBox="0 0 12 12"><rect x="0.5" y="2.5" width="11" height="7" fill="none" stroke="#ff6a00"/><path d="M.5 2.5L6 7l5.5-4.5" fill="none" stroke="#ff6a00"/></svg>
    stay@harboursidelinden
  </div>
  <div class="abs offer">Rooms from only <b>$70</b></div>

  <ul class="abs nav">
    <li class="active" style="width:90px">Homepage</li>
    <li style="width:224px;border-left:1px solid #777;margin-left:12px">Accommodation &amp; Rates</li>
    <li style="width:128px">Facilities</li>
    <li style="width:136px">Attractions</li>
    <li style="width:130px">Bookings</li>
    <li style="flex:1;border-right:none">Contact us</li>
  </ul>

  <div class="abs slider" role="img" aria-label="Hotel lounge photograph with red sofa, white coffee table and bar stools"></div>
  <div class="abs shadow"></div>

  <form class="abs booking">
    <div class="field" style="left:20px;top:18px;width:235px;width:235px;max-width:200px">Select a Room...
      <svg width="9" height="6" viewBox="0 0 9 6" style="top:8px"><path d="M0 0h9L4.5 6z" fill="#555"/></svg></div>
    <div class="field" style="left:20px;top:62px;width:93px">From
      <svg width="11" height="11" viewBox="0 0 11 11"><rect x=".5" y=".5" width="10" height="10" fill="none" stroke="#555"/><path d="M.5 3h10M3.5 3v8M6.5 3v8M.5 5.5h10M.5 8h10" stroke="#555"/></svg></div>
    <div class="field" style="left:126px;top:62px;width:93px">To
      <svg width="11" height="11" viewBox="0 0 11 11"><rect x=".5" y=".5" width="10" height="10" fill="none" stroke="#555"/><path d="M.5 3h10M3.5 3v8M6.5 3v8M.5 5.5h10M.5 8h10" stroke="#555"/></svg></div>
    <div class="abs btn-book">Book Now</div>
  </form>

  <div class="abs section-title"><h2>WHO WE ARE</h2></div>
  <p class="abs about clip">Lorem Ipsum is simply dummy text of the printing and typesetting industry. Lorem Ipsum has been the industry's standard dummy text ever since the 1500s, when an unknown printer took a galley of type and scrambled it to make a type specimen book. It has survived not only five centuries, but also the leap into electronic typesetting, remaining essentially unchanged.</p>
  <p class="abs about full">Lorem Ipsum is simply dummy text of the printing and typesetting industry. Lorem Ipsum has been the industry's standard dummy text ever since the 1500s, when an unknown printer took a galley of type and scrambled it to make a type specimen book. It has survived not only five centuries, but also the leap into electronic typesetting, remaining essentially unchanged. It was popularised in the 1960s with the release of Typeline sheets containing Lorem Ipsum passages, and more recently with desktop publishing software like Pageset Studio including versions of Lorem Ipsum.</p>
  <div class="abs more lg">read more
    <svg width="26" height="10" viewBox="0 0 26 10"><path d="M0 5h24M19 1l5 4-5 4" fill="none" stroke="#fff" stroke-width="1.6"/></svg></div>

  <div class="abs card" style="left:18px;top:804px">
    <h3>OUR FACILITIES</h3><div class="rule"></div>
    <div class="frame"><div role="img" aria-label="Hotel bar with stools and pool table" style="background:linear-gradient(180deg,#7a4a3a,#8c2a25 60%,#2f8f3a)"></div></div>
    <p><b>Lorem Ipsum is simply dummy text of the printing and typesetting</b> industry. Lorem Ipsum has been the industry's standard dummy text ever since the 1500s, when an unknown printer took a galley of type and scrambled it to make a type specimen book...</p>
    <div class="more sm">read more <svg width="18" height="9" viewBox="0 0 18 9"><path d="M0 4.5h16M12 1l4 3.5-4 3.5" fill="none" stroke="#fff" stroke-width="1.5"/></svg></div>
  </div>

  <div class="abs card" style="left:300px;top:804px">
    <h3>OUR ATTRACTIONS</h3><div class="rule"></div>
    <div class="frame"><div role="img" aria-label="Guest room with bunk beds and small fridge" style="background:linear-gradient(180deg,#b8a58a,#d9d0c2 55%,#c9c9d2)"></div></div>
    <p><b>Lorem Ipsum is simply dummy text of the printing and typesetting</b> industry. Lorem Ipsum has been the industry's standard dummy text ever since the 1500s, when an unknown printer took a galley of type and scrambled it to make a type specimen book...</p>
    <div class="more sm">read more <svg width="18" height="9" viewBox="0 0 18 9"><path d="M0 4.5h16M12 1l4 3.5-4 3.5" fill="none" stroke="#fff" stroke-width="1.5"/></svg></div>
  </div>

  <div class="abs card" style="left:584px;top:806px">
    <h3>BOKKING</h3><div class="rule"></div>
    <div class="frame"><div role="img" aria-label="Brick courtyard with picnic table" style="background:linear-gradient(180deg,#9a4a32,#8a6a55 55%,#c8b79a)"></div></div>
    <p><b>Lorem Ipsum is simply dummy text of the printing and typesetting</b> industry. Lorem Ipsum has been the industry's standard dummy text ever since the 1500s, when an unknown printer took a galley of type and scrambled it to make a type specimen book...</p>
    <div class="more sm">read more <svg width="18" height="9" viewBox="0 0 18 9"><path d="M0 4.5h16M12 1l4 3.5-4 3.5" fill="none" stroke="#fff" stroke-width="1.5"/></svg></div>
  </div>

  <footer class="abs footer">
    <span>Copyright © 2013 Bluegum Studio . Powered by Pressline</span>
    <nav><span>Contact Us</span><i>|</i><span>Terms &amp; Policies</span><i>|</i><span>FAQs</span><i>|</i><span>Terms of Use</span></nav>
  </footer>
</div>
</body>
</html>
```